Accident Law Firm Billboard Bold Easy to See Car Accidents

We need a billboard design that can catch attention in a very crowed Car Accident lawyer market. We wish to feature the phone number (652) 318-4470 as the focus of the Bill Board. We are trying to get the phone number recognized and remembered by drivers. The law firm name is not as crucial to remember.
Basically, It's CAR ACCIDENT? Then (652) 318-4470. We are not married to any specific color scheme but it has to POP and catch attention.
So the Crucial elements are as follows:
1. Phone number (652) 318-4470
2. Words CAR ACCIDENT?
3. Firm Logo in lower portion or where appropriate. Firm Logo to be provided
4. We may want to try a Day Glow orange color, with White and Black added. An example of the color scheme shall be provided.
5. Possible "Catch Phrase" to be used, "It's Time Call 9"
Target Market(s)
Orlando Florida Car Accident victims
Industry/Entity Type
Law Firm
Requirements
Must have
- Easy to see phone number (652) 318-4470
- Catch attention
Nice to have
- I would like to have the sign visible in bright sunlight and it not too hard to immediately know what phone number is for
Should not have
- too many words
- No bold enough
- confusing fonts
- Unclear fonts

```html
<!DOCTYPE html>
<html lang="en">
<head>
<meta charset="utf-8">
<title>Car Accident Billboards</title>
<link href="https://fonts.googleapis.com/css2?family=Oswald:wght@500;600&family=Open+Sans:wght@400;700;800&display=swap" rel="stylesheet">
<style>
  :root {
    --orange: #f6822a;
    --orange-deep: #e8681a;
    --black: #1b1b1b;
    --white: #ffffff;
    --page: #f1f1f1;
    --caption: #555555;
  }
  * { box-sizing: border-box; margin: 0; padding: 0; }
  html, body { width: 783px; height: 1200px; overflow: hidden; }
  body { background: var(--page); position: relative; font-family: "Open Sans", Arial, sans-serif; }

  .billboard { position: absolute; left: 91px; width: 609px; height: 334px; overflow: hidden; }
  .billboard--one { top: 18px; background: var(--orange); }
  .billboard--two { top: 414px; background: var(--white); }
  .billboard--three { top: 812px; background: radial-gradient(ellipse at 50% 30%, #f79244 0%, var(--orange) 55%, var(--orange-deep) 100%); }

  .caption { position: absolute; right: 70px; font-size: 11px; color: var(--caption); letter-spacing: 0.5px; }

  .headline {
    position: absolute; left: 0; width: 100%; text-align: center; white-space: nowrap;
    font-family: "Oswald", "Arial Narrow", sans-serif; font-weight: 600;
    font-size: 88px; line-height: 1; color: var(--white); letter-spacing: 1px;
    transform: scaleY(1.25); transform-origin: top center;
  }
  .headline .accent { color: var(--orange); }
  .headline .dark { color: var(--black); }

  .phone { display: flex; align-items: center; font-weight: 800; color: var(--white); letter-spacing: 1px; white-space: nowrap; }
  .phone-icon { flex: none; }

  .tagline { font-weight: 400; color: var(--white); white-space: nowrap; }
  .tagline strong { font-weight: 800; }

  .firm { font-weight: 800; color: var(--black); line-height: 1.05; white-space: nowrap; }
  .firm span { display: block; font-weight: 400; letter-spacing: 2px; }

  /* sample one */
  .billboard--one .headline { top: 22px; }
  .billboard--one .band { position: absolute; left: 0; top: 168px; width: 100%; height: 82px; background: var(--black); }
  .billboard--one .phone { position: absolute; left: 28px; top: 8px; font-size: 56px; }
  .billboard--one .phone-icon { margin-right: 20px; }
  .billboard--one .tagline { position: absolute; left: 28px; top: 262px; font-size: 44px; }
  .billboard--one .divider { position: absolute; left: 420px; top: 272px; width: 2px; height: 44px; background: var(--white); }
  .billboard--one .firm { position: absolute; left: 436px; top: 274px; font-size: 22px; color: var(--white); }
  .billboard--one .firm span { font-size: 13px; }

  /* sample two */
  .billboard--two .headline { top: 18px; }
  .billboard--two .band { position: absolute; left: 0; top: 152px; width: 100%; height: 84px; background: var(--orange); }
  .billboard--two .tagline { position: absolute; left: 24px; top: 8px; font-size: 54px; }
  .billboard--two .firm { position: absolute; left: 22px; top: 256px; font-size: 32px; }
  .billboard--two .firm span { font-size: 18px; }
  .billboard--two .phone-bar { position: absolute; left: 205px; top: 236px; width: 404px; height: 98px; background: var(--black); clip-path: polygon(12% 0, 100% 0, 100% 100%, 0 100%); }
  .billboard--two .phone { position: absolute; left: 54px; top: 26px; font-size: 34px; }
  .billboard--two .phone-icon { margin-right: 12px; }

  /* sample three */
  .billboard--three .headline { top: 22px; }
  .billboard--three .phone { position: absolute; left: 40px; top: 160px; font-size: 54px; }
  .billboard--three .phone-icon { margin-right: 22px; }
  .billboard--three .foot { position: absolute; left: 0; top: 250px; width: 100%; height: 84px; background: var(--white); }
  .billboard--three .firm { position: absolute; left: 20px; top: 12px; font-size: 28px; }
  .billboard--three .firm span { font-size: 16px; }
  .billboard--three .tag-bar { position: absolute; left: 200px; top: 0; width: 409px; height: 84px; background: var(--black); clip-path: polygon(10% 0, 100% 0, 100% 100%, 0 100%); }
  .billboard--three .tagline { position: absolute; left: 48px; top: 14px; font-size: 40px; color: var(--orange); }
  .billboard--three .tagline strong { color: var(--white); }
</style>
</head>
<body>

<section class="billboard billboard--one">
  <h1 class="headline">CAR ACCIDENT?</h1>
  <div class="band">
    <div class="phone">
      <svg class="phone-icon" width="50" height="50" viewBox="0 0 52 52" aria-hidden="true">
        <circle cx="26" cy="26" r="26" fill="#f6822a"/>
        <path d="M21 14c-3 1-5 4-4 9 1 6 5 12 10 15 3 2 6 1 8-1l-4-5-3 1c-2-1-4-5-5-8l2-2z" fill="#1b1b1b"/>
      </svg>
      (652) 318-4470
    </div>
  </div>
  <p class="tagline">IT'S TIME <strong>CALL 9</strong></p>
  <div class="divider"></div>
  <p class="firm">MARVELLI<span>LAW FIRM P.C.</span></p>
</section>
<p class="caption" style="top:360px;">BILLBOARD SAMPLE 1</p>

<section class="billboard billboard--two">
  <h1 class="headline"><span class="accent">CAR</span> <span class="dark">ACCIDENT?</span></h1>
  <div class="band">
    <p class="tagline">IT'S TIME <strong>CALL 9</strong></p>
  </div>
  <p class="firm">MARVELLI<span>LAW FIRM P.C.</span></p>
  <div class="phone-bar">
    <div class="phone">
      <svg class="phone-icon" width="36" height="36" viewBox="0 0 52 52" aria-hidden="true">
        <circle cx="26" cy="26" r="26" fill="#f6822a"/>
        <path d="M21 14c-3 1-5 4-4 9 1 6 5 12 10 15 3 2 6 1 8-1l-4-5-3 1c-2-1-4-5-5-8l2-2z" fill="#1b1b1b"/>
      </svg>
      (652) 318-4470
    </div>
  </div>
</section>
<p class="caption" style="top:757px;">BILLBOARD SAMPLE 2</p>

<section class="billboard billboard--three">
  <h1 class="headline">CAR ACCIDENT?</h1>
  <div class="phone">
    <svg class="phone-icon" width="48" height="48" viewBox="0 0 52 52" aria-hidden="true">
      <circle cx="26" cy="26" r="26" fill="#1b1b1b"/>
      <path d="M21 14c-3 1-5 4-4 9 1 6 5 12 10 15 3 2 6 1 8-1l-4-5-3 1c-2-1-4-5-5-8l2-2z" fill="#ffffff"/>
    </svg>
    (652) 318-4470
  </div>
  <div class="foot">
    <p class="firm">MARVELLI<span>LAW FIRM P.C.</span></p>
    <div class="tag-bar">
      <p class="tagline">IT'S TIME <strong>CALL 9</strong></p>
    </div>
  </div>
</section>
<p class="caption" style="top:1166px;">BILLBOARD SAMPLE 3</p>

</body>
</html>
```